Design 2015 Winter themed holiday card

We need a holiday card for our company.

The attached brief provides all the information for the design. We provided two images for the cover or if you have something better.

CARD DESIGN 4" x 6" Vertical Folded Card
Bleed: The extra .0625" on each side of your artwork that bleeds off the edge of the piece and ensures your piece will not end up with white borders.
Trim: The final size the printed piece will be.
Safe: The .0625" area from the final trim size. Do not place text or important imagery beyond the safe line to avoid it getting cut off when the finished piece is trimmed to final size.
Corner Rounding, where available, can be 1/8" or 5/16". Examples are provided in the image below.
1/8" is a "tighter" or "smaller" corner radius.
5/16" is a "wider" or "larger" corner radius.

Target Market(s)

Government agencies, businesses and nonprofits

Industry/Entity Type

It Company

Font styles to use
Serif
Sans Serif

Requirements
Must have
• Please follow the design brief: KQRB-Strategy-Brief-Holiday-Card-11042015.pdf
• It includes the fonts, colors, design parameters - please review it before designing. I've included two previous holiday cards for your review.
• Please add "Seasons Greetings" on the cover.

```html
<!DOCTYPE html>
<html lang="en">
<head>
<meta charset="utf-8">
<title>KQRB Holiday Card</title>
<link href="https://fonts.googleapis.com/css2?family=Raleway:wght@400;700&family=Cormorant+SC:wght@500&family=Cookie&family=Marck+Script&family=Arimo:wght@400;700&display=swap" rel="stylesheet">
<style>
  :root {
    --backdrop: #dcdcdd;
    --paper: #ffffff;
    --sky-top: #6775bd;
    --sky-mid: #95a2d6;
    --snow: #c6d0ec;
    --ink-blue: #4a5aa8;
    --snow-white: #eef1fb;
    --text-grey: #555555;
    --sign-ink: #3d3d3d;
  }
  html, body { margin: 0; padding: 0; }
  body {
    width: 1200px; height: 1000px; overflow: hidden;
    background: var(--backdrop); position: relative;
    font-family: "Raleway", sans-serif;
  }
  .card-panel {
    position: absolute; left: 253px; width: 693px; height: 461px;
    background: var(--paper); border-radius: 12px; overflow: hidden;
    box-shadow: 0 1px 3px rgba(0,0,0,.08);
  }
  .outside { top: 34px; }
  .inside { top: 504px; }

  .back-cover { position: absolute; left: 0; top: 0; width: 347px; height: 100%; text-align: center; }
  .brand-name {
    position: absolute; top: 218px; left: 0; width: 100%;
    font-family: "Raleway", sans-serif; font-weight: 700; font-size: 44px;
    color: var(--ink-blue); letter-spacing: 2px;
  }
  .contact {
    position: absolute; top: 351px; left: 0; width: 100%;
    font-family: "Arimo", sans-serif; font-size: 11px; line-height: 13.5px; color: var(--text-grey);
  }
  .contact .company { font-weight: 700; }
  .web {
    position: absolute; top: 427px; left: 0; width: 100%;
    font-family: "Arimo", sans-serif; font-size: 11px; color: var(--text-grey);
  }

  .front-cover {
    position: absolute; left: 347px; top: 0; width: 346px; height: 100%;
    background: linear-gradient(180deg, var(--sky-top) 0%, var(--sky-mid) 45%, var(--snow) 68%, var(--snow) 100%);
  }
  .greeting-title {
    position: absolute; top: 98px; left: 0; width: 100%; text-align: center;
    font-family: "Cookie", cursive; font-size: 46px; color: var(--snow-white); margin: 0; font-weight: 400;
  }
  .blessing {
    position: absolute; top: 324px; left: 0; width: 100%; text-align: center;
    font-family: "Cormorant SC", serif; font-weight: 500; font-size: 13px; line-height: 15.8px;
    color: var(--ink-blue); margin: 0;
  }
  .blessing-source {
    position: absolute; top: 430px; left: 0; width: 100%; text-align: center;
    font-family: "Cormorant SC", serif; font-size: 9px; color: var(--ink-blue);
  }

  .signatures { position: absolute; left: 0; top: 0; width: 347px; height: 100%; }
  .signature {
    position: absolute; font-family: "Marck Script", cursive; font-size: 25px;
    color: var(--sign-ink); white-space: nowrap;
  }
  .message {
    position: absolute; left: 347px; top: 106px; width: 346px; text-align: center;
    font-size: 14px; line-height: 26px; color: var(--text-grey); margin: 0;
  }
  .message + .message { top: 206px; }
  .holiday-title {
    position: absolute; left: 347px; top: 312px; width: 346px; text-align: center;
    font-family: "Cookie", cursive; font-size: 54px; color: var(--ink-blue); margin: 0; font-weight: 400;
  }
  .team-line {
    position: absolute; left: 347px; top: 395px; width: 346px; text-align: center;
    font-size: 12px; color: var(--text-grey);
  }
</style>
</head>
<body>
  <section class="card-panel outside">
    <div class="back-cover">
      <div class="brand-name">KQRB</div>
      <div class="contact">
        <div class="company">Kestrel Quay River Bureau,<br>LLC</div>
        418 Larkfield Avenue, Suite 12<br>
        Millbrook, OR 97000<br>
        800-555-0148
      </div>
      <div class="web">kestrelquayriver.com</div>
    </div>
    <div class="front-cover" role="img" aria-label="Winter illustration: snowflakes in a blue sky, snowy pine forest and a small cabin beside a winding stream">
      <h1 class="greeting-title">Seasons Greetings</h1>
      <p class="blessing">We call upon the water<br>that rim the earth, horizon to horizon,<br>that flow in our rivers and streams,<br>that fall upon our garden and fields,<br>and we ask that<br>they teach and show us the way.</p>
      <div class="blessing-source">(Chinook Blessing Litany)</div>
    </div>
  </section>

  <section class="card-panel inside">
    <div class="signatures">
      <span class="signature" style="left:64px;top:62px;font-size:28px">Owen Marsh</span>
      <span class="signature" style="left:165px;top:106px;color:#666">Greta Lindell</span>
      <span class="signature" style="left:44px;top:152px">Nora Pell</span>
      <span class="signature" style="left:155px;top:198px;color:#555">Ines Carver</span>
      <span class="signature" style="left:48px;top:242px">Tobias Renn</span>
      <span class="signature" style="left:170px;top:284px">Mila Ostrand</span>
      <span class="signature" style="left:46px;top:322px;color:#555">Clara Vosk</span>
      <span class="signature" style="left:162px;top:366px">Peter Hollis</span>
    </div>
    <p class="message">As this year draws to a close,<br>we are grateful for the opportunities<br>we have had to work together.</p>
    <p class="message">We wish you all the best for<br>the year to come.</p>
    <h2 class="holiday-title">Happy Holidays</h2>
    <div class="team-line">from the Kestrel Quay River Bureau team.</div>
  </section>
</body>
</html>
```